Android Payment Application UI Design

We require a UI/UX design for an existing Android card-based payment application.

We're looking to improve the look + feel of the existing app. What we're after:
- Colour palette options
- Fonts
- Icons

See attached document for existing screen types, icons, etc.

All resources provided must be royalty free.

It's to run on a specialised device, with 720 x 1280 pixel resolution, in portrait only (landscape not required).

Please provide mockup examples of the new screen layout applied to the existing screens in the document.

Target Market(s)

Retail business users

Font styles to use
Sans Serif

Colors

Designer to choose colors to be used in the design.

Requirements
Must have
• Looking for
• - modern design
• - simple colours, easy-to-read sans-serif fonts
• - cohesive, consistent design between screens

```html
<!DOCTYPE html>
<html lang="en">
<head>
<meta charset="utf-8">
<title>Card Payment App – Screen Set</title>
<link href="https://fonts.googleapis.com/css2?family=Roboto:wght@400;500&display=swap" rel="stylesheet">
<style>
  :root{
    --primary:#2f7dcb;
    --primary-dark:#2a72bf;
    --nav:#1b5796;
    --surface:#ffffff;
    --bg:#e3effb;
    --bg-soft:#eef5fd;
    --text:#2f7bc9;
    --text-soft:#8fb8e2;
    --line:#d6e6f6;
    --bar:#5a9ad8;
    --button:#3f8fe0;
    --on-primary:#ffffff;
  }
  *{box-sizing:border-box;margin:0;padding:0}
  html,body{width:1200px;height:1200px;overflow:hidden;background:#fff}
  body{font-family:"Roboto",Arial,sans-serif;color:var(--text)}
  .board{position:absolute;left:0;top:0;width:1500px;height:1500px;transform:scale(.8);transform-origin:0 0}
  .phone{position:absolute;width:348px;height:618px;background:var(--bg);overflow:hidden;box-shadow:0 2px 6px rgba(40,110,190,.15)}
  .abs{position:absolute;white-space:nowrap}
  svg.ic{display:block}
  .status{position:absolute;left:0;top:0;width:100%;height:22px;background:var(--primary-dark);color:var(--on-primary);display:flex;justify-content:flex-end;align-items:center;gap:4px;padding-right:8px;font-size:14px}
  .status svg{width:16px;height:14px}
  .appbar{position:absolute;left:0;top:22px;width:100%;height:55px;background:var(--primary);color:var(--on-primary);box-shadow:0 2px 4px rgba(30,90,160,.25)}
  .appbar.tall{height:102px}
  .appbar .title{position:absolute;left:69px;top:16px;font-size:19px;font-weight:500}
  .appbar .ic{position:absolute;width:24px;height:24px;color:var(--on-primary)}
  .tabs{position:absolute;left:0;top:55px;width:100%;height:47px;display:flex}
  .tabs span{flex:1;text-align:center;font-size:13px;letter-spacing:.5px;line-height:47px;color:rgba(255,255,255,.8)}
  .tabs span.on{color:#fff;font-weight:500}
  .tabs .indicator{position:absolute;left:0;bottom:0;height:3px;background:#fff}
  .navbar{position:absolute;left:0;bottom:0;width:100%;height:47px;background:var(--nav);display:flex;justify-content:space-around;align-items:center;padding:0 55px}
  .navbar svg{width:20px;height:20px;color:#fff}
  .card{position:absolute;background:var(--surface);box-shadow:0 1px 3px rgba(40,110,190,.2)}
  .img-ic{position:absolute;width:40px;height:32px;color:var(--text)}
  .t-sm{font-size:11px;color:var(--text-soft)}
  .t-md{font-size:14px;color:var(--text)}
  .t-lg{font-size:15px;color:var(--text);line-height:19px}
  .star{position:absolute;width:20px;height:20px;color:var(--text)}
  .rating{position:absolute;display:flex;align-items:center;gap:1px;font-size:11px;color:var(--text-soft)}
  .rating svg{width:13px;height:13px;color:#1f5f9f}
  .rating svg.dim{color:#b4cfea}
  .rating b{font-weight:400;margin-left:5px}
  .toggle{position:absolute;width:34px;height:14px;border-radius:7px;background:#d8e7f6}
  .toggle i{position:absolute;top:-4px;left:-4px;width:22px;height:22px;border-radius:50%;background:#e6f0fa;box-shadow:0 1px 2px rgba(0,0,0,.15)}
  .toggle.on{background:#8ec0ef}
  .toggle.on i{left:16px;background:var(--button)}
  .divider{position:absolute;height:1px;background:var(--line)}
  .checkbox{position:absolute;width:17px;height:17px;border:2px solid #9ec3e8;border-radius:2px}
  .checkbox.on{background:var(--button);border-color:var(--button)}
  .checkbox.on svg{width:13px;height:13px;color:#fff}
  .bar{position:absolute;left:0;width:100%;height:46px;background:var(--bar);color:#fff;font-size:14px}
  .avatar{position:absolute;border-radius:50%;background:#dbe9f7;overflow:hidden}
  .btn{position:absolute;left:84px;width:178px;height:35px;background:var(--button);color:#fff;font-size:13px;letter-spacing:.5px;box-shadow:0 1px 3px rgba(30,90,160,.3)}
</style>
</head>
<body>
<svg width="0" height="0" style="position:absolute">
  <symbol id="i-image" viewBox="0 0 40 32"><rect x="1.5" y="1.5" width="37" height="29" fill="none" stroke="currentColor" stroke-width="2.5"/><path d="M6 26l9-11 7 7 5-5 7 9" fill="none" stroke="currentColor" stroke-width="2.5" stroke-linejoin="round"/><circle cx="26" cy="9" r="3" fill="none" stroke="currentColor" stroke-width="2"/></symbol>
  <symbol id="i-star" viewBox="0 0 24 24"><path d="M12 2.5l2.9 6.3 6.9.7-5.2 4.6 1.5 6.8L12 17.4l-6.1 3.5 1.5-6.8-5.2-4.6 6.9-.7z" fill="none" stroke="currentColor" stroke-width="2" stroke-linejoin="round"/></symbol>
  <symbol id="i-star-fill" viewBox="0 0 24 24"><path d="M12 2.5l2.9 6.3 6.9.7-5.2 4.6 1.5 6.8L12 17.4l-6.1 3.5 1.5-6.8-5.2-4.6 6.9-.7z" fill="currentColor"/></symbol>
  <symbol id="i-menu" viewBox="0 0 24 24"><path d="M3 6h18M3 12h18M3 18h18" stroke="currentColor" stroke-width="2"/></symbol>
  <symbol id="i-search" viewBox="0 0 24 24"><circle cx="10" cy="10" r="6" fill="none" stroke="currentColor" stroke-width="2.4"/><path d="M14.5 14.5L21 21" stroke="currentColor" stroke-width="2.6"/></symbol>
  <symbol id="i-filter" viewBox="0 0 24 24"><path d="M3 6h18M6 12h12M10 18h4" stroke="currentColor" stroke-width="2"/></symbol>
  <symbol id="i-arrow" viewBox="0 0 24 24"><path d="M20 12H5M11 5l-7 7 7 7" fill="none" stroke="currentColor" stroke-width="2.2"/></symbol>
  <symbol id="i-dots" viewBox="0 0 24 24"><circle cx="12" cy="5" r="2" fill="currentColor"/><circle cx="12" cy="12" r="2" fill="currentColor"/><circle cx="12" cy="19" r="2" fill="currentColor"/></symbol>
  <symbol id="i-close" viewBox="0 0 24 24"><path d="M5 5l14 14M19 5L5 19" stroke="currentColor" stroke-width="2.2"/></symbol>
  <symbol id="i-caret" viewBox="0 0 24 24"><path d="M6 9h12l-6 7z" fill="currentColor"/></symbol>
  <symbol id="i-check" viewBox="0 0 24 24"><path d="M4 12l5 5 11-11" fill="none" stroke="currentColor" stroke-width="3"/></symbol>
  <symbol id="i-nav-back" viewBox="0 0 24 24"><path d="M19 3v18L4 12z" fill="none" stroke="currentColor" stroke-width="3.4" stroke-linejoin="round"/></symbol>
  <symbol id="i-nav-home" viewBox="0 0 24 24"><circle cx="12" cy="12" r="6.5" fill="none" stroke="currentColor" stroke-width="3.4"/></symbol>
  <symbol id="i-nav-recent" viewBox="0 0 24 24"><rect x="5" y="5" width="14" height="14" fill="none" stroke="currentColor" stroke-width="3.4"/></symbol>
  <symbol id="i-wifi" viewBox="0 0 16 14"><path d="M0 3Q8-3 16 3L8 13z" fill="currentColor"/></symbol>
  <symbol id="i-signal" viewBox="0 0 16 14"><path d="M15 1v12H2z" fill="currentColor"/></symbol>
  <symbol id="i-battery" viewBox="0 0 16 14"><rect x="4" y="1" width="8" height="13" rx="1" fill="currentColor"/><rect x="6" y="0" width="4" height="2" fill="currentColor"/></symbol>
  <symbol id="i-person" viewBox="0 0 80 80"><circle cx="40" cy="32" r="12" fill="currentColor"/><path d="M16 64a24 14 0 0 1 48 0z" fill="currentColor"/></symbol>
</svg>

<main class="board">

  <!-- Discover -->
  <section class="phone" style="left:7px;top:80px">
    <div class="status"><svg><use href="#i-wifi"/></svg><svg><use href="#i-signal"/></svg><svg><use href="#i-battery"/></svg><span>12:30</span></div>
    <header class="appbar tall">
      <svg class="ic" style="left:15px;top:16px"><use href="#i-menu"/></svg>
      <span class="title">Discover</span>
      <svg class="ic" style="left:270px;top:16px"><use href="#i-search"/></svg>
      <svg class="ic" style="left:309px;top:16px"><use href="#i-filter"/></svg>
      <nav class="tabs"><span class="on">FIRST</span><span>SECOND</span><span>THIRD</span><i class="indicator" style="width:116px"></i></nav>
    </header>
    <div class="card" style="left:8px;top:130px;width:332px;height:190px">
      <svg class="img-ic" style="left:146px;top:70px"><use href="#i-image"/></svg>
      <div class="abs t-md" style="left:15px;top:127px;font-size:13px">Short description</div>
      <div class="abs" style="left:15px;top:145px;font-size:23px">Product name</div>
    </div>
    <div class="abs" style="left:23px;top:340px;font-size:15px;font-weight:500">Category</div>
    <div class="abs t-sm" style="left:23px;top:362px;font-size:13px">Descriptive text</div>
    <div class="abs" style="left:285px;top:354px;font-size:13px;font-weight:500;letter-spacing:.5px">MORE</div>
    <div class="card" style="left:8px;top:393px;width:105px;height:200px;background:var(--bg-soft)">
      <div class="abs" style="left:0;top:0;width:105px;height:104px;background:#fff"></div>
      <svg class="img-ic" style="left:42px;top:42px"><use href="#i-image"/></svg>
      <div class="abs t-md" style="left:8px;top:111px;font-size:13px;line-height:16px">Item One Two<br>Three</div>
      <div class="abs t-sm" style="left:8px;top:145px">Category</div>
      <div class="abs t-sm" style="right:8px;top:167px">$110</div>
    </div>
    <div class="card" style="left:122px;top:393px;width:105px;height:200px;background:var(--bg-soft)">
      <div class="abs" style="left:0;top:0;width:105px;height:104px;background:#fff"></div>
      <svg class="img-ic" style="left:42px;top:42px"><use href="#i-image"/></svg>
      <div class="abs t-md" style="left:8px;top:111px;font-size:13px;line-height:16px">Item One Two<br>Three</div>
      <div class="abs t-sm" style="left:8px;top:145px">Category</div>
      <div class="abs t-sm" style="right:8px;top:167px">$110</div>
    </div>
    <div class="card" style="left:235px;top:393px;width:105px;height:200px;background:var(--bg-soft)">
      <div class="abs" style="left:0;top:0;width:105px;height:104px;background:#fff"></div>
      <svg class="img-ic" style="left:42px;top:42px"><use href="#i-image"/></svg>
      <div class="abs t-md" style="left:8px;top:111px;font-size:13px;line-height:16px">Item One Two<br>Three</div>
      <div class="abs t-sm" style="left:8px;top:145px">Category</div>
      <div class="abs t-sm" style="right:8px;top:167px">$110</div>
    </div>
    <nav class="navbar"><svg><use href="#i-nav-back"/></svg><svg><use href="#i-nav-home"/></svg><svg><use href="#i-nav-recent"/></svg></nav>
  </section>

  <!-- Category list -->
  <section class="phone" style="left:382px;top:80px">
    <div class="status"><svg><use href="#i-wifi"/></svg><svg><use href="#i-signal"/></svg><svg><use href="#i-battery"/></svg><span>12:30</span></div>
    <header class="appbar tall">
      <svg class="ic" style="left:15px;top:16px"><use href="#i-arrow"/></svg>
      <span class="title">Category</span>
      <svg class="ic" style="left:270px;top:16px"><use href="#i-search"/></svg>
      <svg class="ic" style="left:309px;top:16px"><use href="#i-filter"/></svg>
      <nav class="tabs"><span class="on">FIRST</span><span>SECOND</span><span>THIRD</span><i class="indicator" style="width:116px"></i></nav>
    </header>
    <article class="card" style="left:8px;top:130px;width:332px;height:132px">
      <svg class="img-ic" style="left:30px;top:50px"><use href="#i-image"/></svg>
      <div class="abs t-sm" style="left:114px;top:14px">Item</div>
      <div class="abs t-lg" style="left:114px;top:29px">Vitae lectus erat mollit odio<br>luctus aenean sit dapibus</div>
      <div class="abs t-md" style="left:114px;top:73px">$120</div>
      <div class="rating" style="left:114px;top:100px"><svg><use href="#i-star-fill"/></svg><svg><use href="#i-star-fill"/></svg><svg><use href="#i-star-fill"/></svg><svg><use href="#i-star-fill"/></svg><svg class="dim"><use href="#i-star-fill"/></svg><b>134</b></div>
      <svg class="star" style="left:298px;top:98px"><use href="#i-star"/></svg>
    </article>
    <article class="card" style="left:8px;top:270px;width:332px;height:132px">
      <svg class="img-ic" style="left:30px;top:50px"><use href="#i-image"/></svg>
      <div class="abs t-sm" style="left:114px;top:14px">Item</div>
      <div class="abs t-lg" style="left:114px;top:29px">Vestibulum nam in tempus<br>sed magnis massa</div>
      <div class="abs t-md" style="left:114px;top:73px">$120</div>
      <div class="rating" style="left:114px;top:100px"><svg><use href="#i-star-fill"/></svg><svg><use href="#i-star-fill"/></svg><svg><use href="#i-star-fill"/></svg><svg><use href="#i-star-fill"/></svg><svg class="dim"><use href="#i-star-fill"/></svg><b>134</b></div>
      <svg class="star" style="left:298px;top:98px"><use href="#i-star"/></svg>
    </article>
    <article class="card" style="left:8px;top:409px;width:332px;height:132px">
      <svg class="img-ic" style="left:30px;top:50px"><use href="#i-image"/></svg>
      <div class="abs t-sm" style="left:114px;top:14px">Item</div>
      <div class="abs t-lg" style="left:114px;top:29px">Blandit quam velit venenatis<br>leo ante justo leo</div>
      <div class="abs t-md" style="left:114px;top:73px">$120</div>
      <div class="rating" style="left:114px;top:100px"><svg><use href="#i-star-fill"/></svg><svg><use href="#i-star-fill"/></svg><svg><use href="#i-star-fill"/></svg><svg><use href="#i-star-fill"/></svg><svg class="dim"><use href="#i-star-fill"/></svg><b>134</b></div>
      <svg class="star" style="left:298px;top:98px"><use href="#i-star"/></svg>
    </article>
    <article class="card" style="left:8px;top:548px;width:332px;height:60px">
      <div class="abs t-sm" style="left:114px;top:14px">Item</div>
    </article>
    <nav class="navbar"><svg><use href="#i-nav-back"/></svg><svg><use href="#i-nav-home"/></svg><svg><use href="#i-nav-recent"/></svg></nav>
  </section>

  <!-- Cart -->
  <section class="phone" style="left:759px;top:80px">
    <div class="status"><svg><use href="#i-wifi"/></svg><svg><use href="#i-signal"/></svg><svg><use href="#i-battery"/></svg><span>12:30</span></div>
    <header class="appbar">
      <svg class="ic" style="left:15px;top:16px"><use href="#i-menu"/></svg>
      <span class="title" style="left:54px">Cart</span>
      <svg class="ic" style="left:314px;top:16px"><use href="#i-dots"/></svg>
    </header>
    <div class="abs" style="left:0;top:77px;width:348px;height:255px;background:#fff"></div>
    <div class="abs" style="left:8px;top:85px;width:69px;height:69px;background:var(--bg)"><svg class="img-ic" style="left:22px;top:25px;width:26px;height:20px"><use href="#i-image"/></svg></div>
    <div class="abs t-lg" style="left:92px;top:90px">Item one</div>
    <div class="abs t-sm" style="left:92px;top:109px">Category</div>
    <div class="abs t-sm" style="left:92px;top:135px;font-size:12px">QTY: 1</div>
    <svg class="abs" style="left:138px;top:132px;width:16px;height:16px;color:var(--text)"><use href="#i-caret"/></svg>
    <svg class="abs" style="left:318px;top:90px;width:20px;height:20px;color:var(--text)"><use href="#i-dots"/></svg>
    <div class="abs t-md" style="right:16px;top:130px;font-size:13px">$230</div>
    <div class="divider" style="left:8px;top:162px;width:340px"></div>
    <div class="abs" style="left:8px;top:171px;width:69px;height:69px;background:var(--bg)"><svg class="img-ic" style="left:22px;top:25px;width:26px;height:20px"><use href="#i-image"/></svg></div>
    <div class="abs t-lg" style="left:92px;top:176px">Item two</div>
    <div class="abs t-sm" style="left:92px;top:195px">Category</div>
    <div class="abs t-sm" style="left:92px;top:221px;font-size:12px">QTY: 1</div>
    <svg class="abs" style="left:138px;top:218px;width:16px;height:16px;color:var(--text)"><use href="#i-caret"/></svg>
    <svg class="abs" style="left:318px;top:176px;width:20px;height:20px;color:var(--text)"><use href="#i-dots"/></svg>
    <div class="abs t-md" style="right:16px;top:216px;font-size:13px">$230</div>
    <div class="divider" style="left:8px;top:248px;width:340px"></div>
    <div class="abs" style="left:8px;top:257px;width:69px;height:69px;background:var(--bg)"><svg class="img-ic" style="left:22px;top:25px;width:26px;height:20px"><use href="#i-image"/></svg></div>
    <div class="abs t-lg" style="left:92px;top:262px">Item three</div>
    <div class="abs t-sm" style="left:92px;top:281px">Category</div>
    <div class="abs t-sm" style="left:92px;top:306px;font-size:12px">QTY: 1</div>
    <svg class="abs" style="left:138px;top:303px;width:16px;height:16px;color:var(--text)"><use href="#i-caret"/></svg>
    <svg class="abs" style="left:318px;top:262px;width:20px;height:20px;color:var(--text)"><use href="#i-dots"/></svg>
    <div class="abs t-md" style="right:16px;top:302px;font-size:13px">$230</div>
    <div class="bar" style="top:525px"><span class="abs" style="left:15px;top:15px">Total: $1220</span><span class="abs" style="right:13px;top:15px;letter-spacing:.5px">CONTINUE</span></div>
    <nav class="navbar"><svg><use href="#i-nav-back"/></svg><svg><use href="#i-nav-home"/></svg><svg><use href="#i-nav-recent"/></svg></nav>
  </section>

  <!-- Profile settings -->
  <section class="phone" style="left:1141px;top:80px;background:#fff">
    <div class="status"><svg><use href="#i-wifi"/></svg><svg><use href="#i-signal"/></svg><svg><use href="#i-battery"/></svg><span>12:30</span></div>
    <header class="appbar">
      <svg class="ic" style="left:15px;top:16px"><use href="#i-menu"/></svg>
      <span class="title">Profile</span>
      <svg class="ic" style="left:314px;top:16px"><use href="#i-dots"/></svg>
    </header>
    <div class="avatar" style="left:135px;top:100px;width:78px;height:78px"><svg style="width:78px;height:78px;color:var(--button)"><use href="#i-person"/></svg></div>
    <div class="abs" style="left:0;width:348px;top:187px;text-align:center;font-size:22px">User Name</div>
    <div class="abs" style="left:0;width:348px;top:221px;text-align:center;font-size:14px">user@example.com</div>
    <div class="abs t-md" style="left:16px;top:272px;font-size:13px;font-weight:500">Settings</div>
    <div class="divider" style="left:0;top:304px;width:348px"></div>
    <svg class="star" style="left:17px;top:317px"><use href="#i-star"/></svg><div class="abs t-lg" style="left:69px;top:318px">Setting one</div>
    <svg class="star" style="left:17px;top:363px"><use href="#i-star"/></svg><div class="abs t-lg" style="left:69px;top:364px">Setting two</div>
    <div class="toggle" style="left:296px;top:367px"><i></i></div>
    <svg class="star" style="left:17px;top:410px"><use href="#i-star"/></svg><div class="abs t-lg" style="left:69px;top:411px">Setting three</div>
    <div class="toggle on" style="left:296px;top:414px"><i></i></div>
    <div class="abs t-md" style="left:16px;top:465px;font-size:13px;font-weight:500">Support</div>
    <div class="divider" style="left:0;top:497px;width:348px"></div>
    <svg class="star" style="left:17px;top:511px"><use href="#i-star"/></svg><div class="abs t-lg" style="left:69px;top:512px">Setting four</div>
    <svg class="star" style="left:17px;top:557px"><use href="#i-star"/></svg><div class="abs t-lg" style="left:69px;top:558px">Setting five</div>
    <nav class="navbar"><svg><use href="#i-nav-back"/></svg><svg><use href="#i-nav-home"/></svg><svg><use href="#i-nav-recent"/></svg></nav>
  </section>

  <!-- Navigation drawer -->
  <section class="phone" style="left:8px;top:732px;background:#bcd7f1">
    <div class="abs" style="left:0;top:22px;width:348px;height:102px;background:#3d84cc"></div>
    <svg class="abs" style="left:309px;top:38px;width:24px;height:24px;color:#9cc3ea"><use href="#i-filter"/></svg>
    <div class="abs" style="left:290px;top:93px;font-size:13px;color:#9cc3ea">RD</div>
    <div class="abs" style="left:0;top:130px;width:340px;height:190px;background:#9fc7ee"></div>
    <div class="abs" style="left:290px;top:354px;font-size:13px;font-weight:500;color:#4f8fd2">MORE</div>
    <div class="abs" style="left:0;top:393px;width:340px;height:180px;background:#a9cdf0"></div>
    <svg class="img-ic" style="left:276px;top:435px;color:#5f9ad6"><use href="#i-image"/></svg>
    <div class="abs" style="left:282px;top:505px;font-size:13px;color:#5f9ad6">e Two</div>
    <div class="abs" style="left:304px;top:560px;font-size:11px;color:#7aaee0">$110</div>
    <div class="status"><svg><use href="#i-wifi"/></svg><svg><use href="#i-signal"/></svg><svg><use href="#i-battery"/></svg><span>12:30</span></div>
    <aside class="abs" style="left:0;top:22px;width:294px;height:549px;background:#fff;box-shadow:2px 0 8px rgba(30,90,160,.3)">
      <div class="abs" style="left:0;top:0;width:294px;height:148px;background:var(--primary);box-shadow:0 2px 4px rgba(30,90,160,.25)">
        <div class="avatar" style="left:16px;top:20px;width:62px;height:62px"><svg style="width:62px;height:62px;color:var(--button)"><use href="#i-person"/></svg></div>
        <div class="abs" style="left:16px;top:97px;font-size:13px;font-weight:500;color:#fff">Full Name</div>
        <div class="abs" style="left:16px;top:117px;font-size:13px;color:#fff">user@example.com</div>
        <svg class="abs" style="left:258px;top:117px;width:16px;height:16px;color:#fff"><use href="#i-caret"/></svg>
      </div>
      <div class="abs" style="left:0;top:148px;width:294px;height:54px;background:var(--bg)"></div>
      <svg class="star" style="left:17px;top:165px"><use href="#i-star"/></svg><div class="abs t-md" style="left:69px;top:167px;font-weight:500;font-size:13px">Option One</div>
      <svg class="star" style="left:17px;top:211px"><use href="#i-star"/></svg><div class="abs t-md" style="left:69px;top:213px;font-weight:500;font-size:13px">Option Two</div>
      <svg class="star" style="left:17px;top:257px"><use href="#i-star"/></svg><div class="abs t-md" style="left:69px;top:259px;font-weight:500;font-size:13px">Option Three</div>
      <svg class="star" style="left:17px;top:304px"><use href="#i-star"/></svg><div class="abs t-md" style="left:69px;top:306px;font-weight:500;font-size:13px">Option Four</div>
      <svg class="star" style="left:17px;top:350px"><use href="#i-star"/></svg><div class="abs t-md" style="left:69px;top:352px;font-weight:500;font-size:13px">Option Five</div>
      <div class="divider" style="left:0;top:396px;width:294px"></div>
      <div class="abs t-md" style="left:15px;top:411px;font-size:13px">Settings</div>
      <svg class="star" style="left:17px;top:454px"><use href="#i-star"/></svg><div class="abs t-md" style="left:69px;top:456px;font-weight:500;font-size:13px">Option Six</div>
      <div class="toggle on" style="left:243px;top:458px"><i></i></div>
      <svg class="star" style="left:17px;top:500px"><use href="#i-star"/></svg><div class="abs t-md" style="left:69px;top:502px;font-weight:500;font-size:13px">Option Seven</div>
      <div class="toggle" style="left:243px;top:504px"><i></i></div>
    </aside>
    <nav class="navbar"><svg><use href="#i-nav-back"/></svg><svg><use href="#i-nav-home"/></svg><svg><use href="#i-nav-recent"/></svg></nav>
  </section>

  <!-- Filter -->
  <section class="phone" style="left:382px;top:732px">
    <div class="status"><svg><use href="#i-wifi"/></svg><svg><use href="#i-signal"/></svg><svg><use href="#i-battery"/></svg><span>12:30</span></div>
    <header class="appbar">
      <svg class="ic" style="left:15px;top:16px"><use href="#i-close"/></svg>
      <span class="title">Filter</span>
    </header>
    <div class="abs t-md" style="left:15px;top:99px;font-size:13px;font-weight:500">Category One</div>
    <div class="card" style="left:8px;top:131px;width:332px;height:174px">
      <div class="checkbox" style="left:19px;top:19px"></div><div class="abs t-md" style="left:69px;top:19px;font-size:13px">Option one</div><div class="abs t-sm" style="right:16px;top:20px;font-size:13px">Description</div>
      <div class="checkbox on" style="left:19px;top:57px"><svg><use href="#i-check"/></svg></div><div class="abs t-md" style="left:69px;top:58px;font-size:13px">Option two</div><div class="abs t-sm" style="right:16px;top:59px;font-size:13px">Description</div>
      <div class="checkbox" style="left:19px;top:96px"></div><div class="abs t-md" style="left:69px;top:97px;font-size:13px">Option three</div><div class="abs t-sm" style="right:16px;top:98px;font-size:13px">Description</div>
      <div class="checkbox" style="left:19px;top:135px"></div><div class="abs t-md" style="left:69px;top:135px;font-size:13px">Evening</div><div class="abs t-sm" style="right:16px;top:136px;font-size:13px">Description</div>
    </div>
    <div class="abs t-md" style="left:15px;top:326px;font-size:13px;font-weight:500">Category Two</div>
    <div class="card" style="left:8px;top:358px;width:332px;height:174px">
      <div class="checkbox" style="left:19px;top:19px"></div><div class="abs t-md" style="left:69px;top:19px;font-size:13px">Option one</div><div class="abs t-sm" style="right:16px;top:20px;font-size:13px">Description</div>
      <div class="checkbox on" style="left:19px;top:57px"><svg><use href="#i-check"/></svg></div><div class="abs t-md" style="left:69px;top:58px;font-size:13px">Option two</div><div class="abs t-sm" style="right:16px;top:59px;font-size:13px">Description</div>
      <div class="checkbox" style="left:19px;top:96px"></div><div class="abs t-md" style="left:69px;top:97px;font-size:13px">Option three</div><div class="abs t-sm" style="right:16px;top:98px;font-size:13px">Description</div>
      <div class="checkbox" style="left:19px;top:135px"></div><div class="abs t-md" style="left:69px;top:135px;font-size:13px">Evening</div><div class="abs t-sm" style="right:16px;top:136px;font-size:13px">Description</div>
    </div>
    <div class="bar" style="top:525px"><span class="abs" style="right:16px;top:15px;letter-spacing:.5px">NEXT</span></div>
    <nav class="navbar"><svg><use href="#i-nav-back"/></svg><svg><use href="#i-nav-home"/></svg><svg><use href="#i-nav-recent"/></svg></nav>
  </section>

  <!-- Sign in -->
  <section class="phone" style="left:755px;top:732px">
    <div class="status"><svg><use href="#i-wifi"/></svg><svg><use href="#i-signal"/></svg><svg><use href="#i-battery"/></svg><span>12:30</span></div>
    <header class="appbar tall">
      <svg class="ic" style="left:15px;top:16px"><use href="#i-menu"/></svg>
      <nav class="tabs"><span class="on">SIGN IN</span><span>SIGN UP</span><i class="indicator" style="width:174px"></i></nav>
    </header>
    <div class="abs" style="left:0;width:348px;top:220px;display:flex;justify-content:center;align-items:center;gap:12px">
      <i style="display:block;width:18px;height:18px;background:var(--text)"></i>
      <span style="font-size:22px">TAPLINE</span>
    </div>
    <p class="abs" style="left:44px;width:260px;top:258px;text-align:center;font-size:15px;line-height:23px;white-space:normal">Aliquip magnis repellat. Scelerisque dignissim at. Ridiculus vehicula erat.</p>
    <div class="btn" style="top:405px"><i class="abs" style="left:18px;top:12px;width:11px;height:11px;background:#fff"></i><span class="abs" style="left:50px;top:10px">CLICK HERE</span></div>
    <div class="btn" style="top:455px"><i class="abs" style="left:18px;top:12px;width:11px;height:11px;background:#fff"></i><span class="abs" style="left:50px;top:10px">CLICK HERE</span></div>
    <div class="abs" style="left:0;width:348px;top:516px;text-align:center;font-size:15px">Continue with mail</div>
    <nav class="navbar"><svg><use href="#i-nav-back"/></svg><svg><use href="#i-nav-home"/></svg><svg><use href="#i-nav-recent"/></svg></nav>
  </section>

  <!-- Profile form -->
  <section class="phone" style="left:1127px;top:732px;background:#fff">
    <div class="status"><svg><use href="#i-wifi"/></svg><svg><use href="#i-signal"/></svg><svg><use href="#i-battery"/></svg><span>12:30</span></div>
    <header class="appbar">
      <svg class="ic" style="left:15px;top:16px"><use href="#i-arrow"/></svg>
      <span class="title">Profile</span>
      <svg class="ic" style="left:314px;top:16px"><use href="#i-dots"/></svg>
    </header>
    <div class="abs t-sm" style="left:16px;top:101px">Country</div>
    <div class="abs t-lg" style="left:16px;top:120px">Country Name</div>
    <div class="divider" style="left:16px;top:146px;width:317px"></div>
    <div class="abs t-sm" style="left:16px;top:170px">Name</div>
    <div class="abs t-lg" style="left:16px;top:189px">Name Lastname</div>
    <div class="divider" style="left:16px;top:215px;width:317px"></div>
    <div class="abs t-sm" style="left:16px;top:240px">Phone number</div>
    <div class="abs t-lg" style="left:16px;top:259px">+ 7 (900) 123 45 67</div>
    <div class="divider" style="left:16px;top:285px;width:317px"></div>
    <div class="abs t-sm" style="left:16px;top:309px">City</div>
    <div class="abs t-lg" style="left:16px;top:328px">City Name</div>
    <div class="divider" style="left:16px;top:354px;width:317px"></div>
    <div class="abs t-sm" style="left:16px;top:379px">Address</div>
    <div class="abs t-lg" style="left:16px;top:398px">123 Street Name</div>
    <div class="divider" style="left:16px;top:424px;width:317px"></div>
    <nav class="navbar"><svg><use href="#i-nav-back"/></svg><svg><use href="#i-nav-home"/></svg><svg><use href="#i-nav-recent"/></svg></nav>
  </section>

</main>
</body>
</html>
```